Crestwell Renewal Business Card Design Phase 2

Professional and clean design. The design colors should flow with the logo. Two-sided card with the website on the back which is:

www.CrestwellRenewal.example.

"Specializing in Water Damage Restoration"

On the front I need the name, email, phone, and logo.

Name: Dorian Halvek
Email: Dorian@CrestwellRenewal.example
Phone: 555-318-2046 for now

I only have the Preview and Thumbnail right now but should have the source files uploaded within a day or two.

Target Market(s)

Flood victims, home owners with water damage from busted pipes etc...

Industry/Entity Type

Business

Contact Information for Business Card

Name: Dorian Halvek

Font styles to use
Serif
Sans Serif

Requirements
Must have
• Business Card Details Info

```html
<!DOCTYPE html>
<html lang="en">
<head>
<meta charset="utf-8">
<title>Crestwell Renewal Business Card</title>
<link href="https://fonts.googleapis.com/css2?family=Open+Sans:wght@400;600;700&display=swap" rel="stylesheet">
<style>
  :root {
    --navy: #1d3868;
    --green: #4f8f3d;
    --ink: #3a3a3a;
    --rule: #c9c9c9;
    --paper: #ffffff;
    --ghost: #f1f1ef;
    --backdrop: #e9e6e2;
  }
  html, body {
    margin: 0;
    padding: 0;
    width: 1200px;
    height: 1000px;
    overflow: hidden;
    background: var(--backdrop);
    font-family: "Open Sans", Arial, sans-serif;
  }
  .card {
    position: absolute;
    left: 265px;
    width: 666px;
    height: 397px;
    background: var(--paper);
    overflow: hidden;
    box-shadow: 0 2px 6px rgba(0,0,0,0.18);
  }
  .card--front { top: 73px; }
  .card--back { top: 532px; }

  .wordmark {
    position: absolute;
    color: var(--navy);
    font-weight: 700;
    text-transform: uppercase;
    line-height: 1;
    letter-spacing: 0.5px;
  }
  .wordmark__line { display: block; }
  .wordmark__dot {
    display: inline-block;
    width: 14px;
    height: 14px;
    border-radius: 50%;
    background: var(--green);
    margin-top: 14px;
  }
  .card--front .wordmark { left: 32px; top: 32px; font-size: 50px; z-index: 1; }

  .backdrop-art {
    position: absolute;
    left: 240px;
    top: 95px;
    width: 420px;
    height: 280px;
    border-radius: 50% 50% 10px 10px / 40% 40% 10px 10px;
    background: radial-gradient(ellipse at 60% 45%, var(--ghost) 0%, rgba(241,241,239,0.6) 55%, rgba(255,255,255,0) 80%);
  }

  .divider {
    position: absolute;
    left: 32px;
    top: 237px;
    width: 409px;
    height: 2px;
    background: var(--rule);
  }
  .holder-name {
    position: absolute;
    right: 32px;
    top: 223px;
    margin: 0;
    font-size: 20px;
    font-weight: 600;
    color: var(--navy);
  }
  .contact {
    position: absolute;
    left: 32px;
    top: 268px;
    margin: 0;
    padding: 0;
    list-style: none;
    font-size: 15.5px;
    color: var(--ink);
  }
  .contact li {
    display: flex;
    align-items: center;
    height: 25.5px;
  }
  .contact svg {
    width: 15px;
    height: 15px;
    margin-right: 7px;
    fill: var(--navy);
  }
  .band {
    position: absolute;
    left: 0;
    bottom: 0;
    width: 666px;
    height: 24px;
  }

  .back-stack {
    position: absolute;
    left: 0;
    right: 0;
    top: 92px;
    text-align: center;
  }
  .card--back .wordmark {
    position: static;
    font-size: 62px;
  }
  .tagline {
    margin: 22px 0 0;
    font-size: 17px;
    font-weight: 600;
    color: var(--green);
  }
  .back-web {
    margin: 8px 0 0;
    font-size: 16px;
    font-weight: 400;
    color: var(--navy);
  }
</style>
</head>
<body>

<section class="card card--front" aria-label="Business card front">
  <div class="backdrop-art" role="img" aria-label="Faint background illustration area"></div>

  <div class="wordmark">
    <span class="wordmark__line">Crestwell</span>
    <span class="wordmark__line">Renewal</span>
    <span class="wordmark__dot" aria-hidden="true"></span>
  </div>

  <div class="divider"></div>
  <h1 class="holder-name">Dorian Halvek</h1>

  <ul class="contact">
    <li>
      <svg viewBox="0 0 16 16" aria-hidden="true"><path d="M1 6c0-2 3-3.5 7-3.5S15 4 15 6v1h-3.5V5.5h-7V7H1z"/><path d="M4 8h8l2 6H2z"/></svg>
      555-318-2046
    </li>
    <li>
      <svg viewBox="0 0 16 16" aria-hidden="true"><path d="M1 3h14v10H1z M2.5 4.5 8 9l5.5-4.5z" fill-rule="evenodd"/></svg>
      Dorian@CrestwellRenewal.example
    </li>
    <li>
      <svg viewBox="0 0 16 16" aria-hidden="true"><circle cx="8" cy="8" r="7"/><path d="M4 5h3v3H4zM9 9h3v3H9z" fill="#fff"/></svg>
      www.CrestwellRenewal.example
    </li>
  </ul>

  <svg class="band" viewBox="0 0 666 24" aria-hidden="true">
    <polygon points="0,0 388,0 366,24 0,24" fill="var(--green)"/>
    <polygon points="390,0 396,0 374,24 368,24" fill="#fff"/>
    <polygon points="398,0 666,0 666,24 376,24" fill="var(--navy)"/>
  </svg>
</section>

<section class="card card--back" aria-label="Business card back">
  <div class="back-stack">
    <div class="wordmark">
      <span class="wordmark__line">Crestwell</span>
      <span class="wordmark__line">Renewal</span>
    </div>
    <p class="tagline">Specializing in Water Damage Restoration</p>
    <p class="back-web">www.CrestwellRenewal.example</p>
  </div>
</section>

</body>
</html>
```